Book Title: Lantern Seasons -- Unwritten Pages of a Quiet Vocation

I am looking for just the book cover design, do not need spine or back cover art.

This book is a memoir and the cover needs to be prepared for print and ebook applications.

The part of the title that follows the dash ("Unwritten Pages of a Quiet Vocation") is not a subtitle but a tag and can be separated from the title itself.

I am inclined to a traditional design with "modern and minimalist" tendencies. I like graphic images that convey the idea of a "journey" or "quest". The memoir is about my pastoral work as a Christian minister but it is not a "religious" book. I do not want churches or any traditional religious symbols on the cover. In fact this book is directed toward those who have little, if any, interest in organized religion of any kind and if that could somehow be captured in the cover art it would be useful.

I am attaching a file with some sample cover art designs that I like or do not like to help guide your thinking. I am open to your interpretation and creative thinking. This book is a labor of love and I want the cover art to reflect my deep thinking on the topic.

```html
<!DOCTYPE html>
<html lang="en">
<head>
<meta charset="utf-8">
<title>Lantern Seasons — Front Cover</title>
<link rel="stylesheet" href="https://fonts.googleapis.com/css2?family=Cinzel:wght@500;600&family=Montserrat:wght@500;600&display=swap">
<style>
  :root {
    --backdrop: #ececea;
    --paper: #ffffff;
    --sky-deep: #4f86c6;
    --sky-mid: #9fbfe0;
    --sky-pale: #e4edf6;
    --ink: #4a4d52;
    --leaf: #2f8a3c;
    --leaf-light: #58b060;
  }
  * { margin: 0; padding: 0; box-sizing: border-box; }
  html, body {
    width: 1200px;
    height: 2460px;
    overflow: hidden;
    background: var(--backdrop);
  }
  .canvas {
    position: relative;
    width: 1200px;
    height: 2460px;
  }
  .cover {
    position: absolute;
    left: 100px;
    top: 480px;
    width: 1000px;
    height: 1500px;
    background: var(--paper);
    overflow: hidden;
    box-shadow: 0 6px 30px rgba(0,0,0,0.12);
  }
  .cover__sky {
    position: absolute;
    inset: 0 0 auto 0;
    height: 900px;
    background:
      radial-gradient(ellipse 60% 40% at 30% 45%, rgba(255,255,255,0.85), transparent 70%),
      radial-gradient(ellipse 50% 35% at 75% 60%, rgba(255,255,255,0.8), transparent 70%),
      linear-gradient(180deg, var(--sky-deep) 0%, var(--sky-mid) 40%, var(--sky-pale) 75%, var(--paper) 100%);
  }
  .cover__emblem {
    position: absolute;
    left: 410px;
    top: 600px;
    width: 180px;
    height: 170px;
    background: linear-gradient(160deg, var(--leaf-light), var(--leaf));
    border-radius: 6px;
  }
  .cover__title {
    position: absolute;
    left: 0;
    right: 0;
    top: 800px;
    text-align: center;
    font-family: "Cinzel", serif;
    font-weight: 600;
    font-size: 112px;
    line-height: 1.0;
    letter-spacing: 2px;
    color: var(--ink);
  }
  .cover__tag {
    position: absolute;
    left: 230px;
    width: 540px;
    top: 1052px;
    padding: 12px 0 12px 40px;
    border: 2px solid var(--leaf);
    font-family: "Montserrat", sans-serif;
    font-weight: 500;
    font-size: 24px;
    color: var(--ink);
    text-align: center;
  }
  .cover__tag-mark {
    position: absolute;
    left: 0;
    top: 0;
    bottom: 0;
    width: 34px;
    background: var(--leaf);
  }
  .cover__author {
    position: absolute;
    left: 0;
    right: 0;
    top: 1190px;
    text-align: center;
    font-family: "Montserrat", sans-serif;
    font-weight: 600;
    font-size: 62px;
    color: var(--ink);
  }
</style>
</head>
<body>
  <main class="canvas">
    <section class="cover">
      <div class="cover__sky" role="img" aria-label="Soft blue sky with drifting white clouds"></div>
      <div class="cover__emblem" role="img" aria-label="Green graphic of two arrows branching apart like a fork in a path"></div>
      <h1 class="cover__title">LANTERN<br>SEASONS</h1>
      <p class="cover__tag"><span class="cover__tag-mark"></span>Unwritten Pages of a Quiet Vocation</p>
      <p class="cover__author">Author Name</p>
    </section>
  </main>
</body>
</html>
```